Become a Mentor - For Musicians, Artists, Producers and Teachers

Here is the full creative brief:

https://files.plenwick.com/sheets/d/4kTqpLm8Wz_2RNa7Hc3Xv91Jd0Gb5YeUsQ6fNo8rTpxa/view?mode=shared

Here is the background image file: https://www.trovecrate.com/sh/83jbwtrmq5dkx2u/BBHn4k7QTf2ZpLeXX-wr9MUHe?dl=0

LOGO:
https://www.trovecrate.com/sh/k472rufmpdo9b6w/BBKLe3RtHY5J-sFQnLZw7Ggma?dl=0

```html
<!DOCTYPE html>
<html lang="en">
<head>
<meta charset="utf-8">
<title>Become a Mentor – Flyer</title>
<link rel="stylesheet" href="https://fonts.googleapis.com/css2?family=Lobster&family=Montserrat:wght@400;600;700;800&display=swap">
<style>
  :root {
    --backdrop: #cbc0ab;
    --cream: #fbf1d4;
    --gold: #e9b56c;
    --amber: #c77a2e;
    --brown: #4a2a15;
    --orange: #f07822;
    --orange-light: #f48d2c;
    --orange-line: #f9a541;
    --ink: #1d1a17;
    --white: #ffffff;
  }
  * { box-sizing: border-box; margin: 0; padding: 0; }
  html, body { width: 1200px; height: 900px; overflow: hidden; }
  body { background: var(--backdrop); position: relative; font-family: "Montserrat", sans-serif; }

  .flyer {
    position: absolute; left: 310px; top: 40px;
    width: 580px; height: 820px;
    background: var(--cream);
    overflow: hidden;
    box-shadow: 0 10px 30px rgba(0,0,0,0.25);
  }
  .flyer__photo {
    position: absolute; inset: 0 0 200px 0;
    background:
      radial-gradient(ellipse at 80% 70%, rgba(74,42,21,0.75), rgba(74,42,21,0) 55%),
      radial-gradient(ellipse at 40% 65%, rgba(199,122,46,0.55), rgba(199,122,46,0) 60%),
      linear-gradient(180deg, var(--cream) 0%, var(--cream) 18%, var(--gold) 55%, var(--amber) 100%);
  }
  .flyer__frame {
    position: absolute; inset: 22px;
    border: 2px solid rgba(255,255,255,0.85);
    pointer-events: none;
  }
  .flyer__bands { position: absolute; inset: 0; }

  .headline {
    position: absolute; top: 64px; left: 0; right: 0;
    text-align: center; color: var(--ink);
  }
  .headline__kicker {
    font-weight: 400; font-size: 20px; letter-spacing: 2px; text-transform: uppercase;
    padding-left: 90px;
  }
  .headline__title {
    font-family: "Lobster", cursive; font-size: 74px; line-height: 1; margin-top: -4px;
  }

  .stamp { position: absolute; left: 380px; top: 285px; width: 170px; height: 170px; }

  .offer {
    position: absolute; left: 0; right: 0; bottom: 0; height: 250px;
    padding: 0 44px; color: var(--white);
  }
  .offer__points { list-style: none; font-weight: 600; font-size: 15px; line-height: 1.45; }
  .offer__call { font-weight: 800; font-size: 60px; letter-spacing: -1px; margin-top: 14px; line-height: 1.05; }
  .offer__web { font-weight: 600; font-size: 19px; margin-top: 10px; }
  .offer__frame {
    position: absolute; left: 22px; right: 22px; bottom: 22px; height: 210px;
    border: 2px solid var(--orange-line); border-top: none;
  }
</style>
</head>
<body>
  <main class="flyer">
    <div class="flyer__photo" role="img" aria-label="Photo of a mentor guiding a young violinist's bow in a warm-lit music room"></div>
    <div class="flyer__frame"></div>

    <svg class="flyer__bands" viewBox="0 0 580 820" width="580" height="820" aria-hidden="true">
      <polygon points="0,470 580,565 580,820 0,820" fill="var(--orange-light)"/>
      <path d="M0,570 C170,560 330,580 580,565 L580,820 L0,820 Z" fill="var(--orange)"/>
    </svg>

    <header class="headline">
      <p class="headline__kicker">Start your career today</p>
      <h1 class="headline__title">Become a Mentor</h1>
    </header>

    <svg class="stamp" viewBox="0 0 170 170" aria-label="Apply now">
      <circle cx="85" cy="85" r="78" fill="none" stroke="var(--white)" stroke-width="4"/>
      <circle cx="85" cy="85" r="68" fill="none" stroke="var(--white)" stroke-width="1.5"/>
      <g fill="var(--white)">
        <polygon points="62,48 64.5,54 71,54 66,58 68,64 62,60 56,64 58,58 53,54 59.5,54"/>
        <polygon points="85,42 87.5,48 94,48 89,52 91,58 85,54 79,58 81,52 76,48 82.5,48"/>
        <polygon points="108,48 110.5,54 117,54 112,58 114,64 108,60 102,64 104,58 99,54 105.5,54"/>
        <polygon points="62,112 64.5,118 71,118 66,122 68,128 62,124 56,128 58,122 53,118 59.5,118"/>
        <polygon points="85,116 87.5,122 94,122 89,126 91,132 85,128 79,132 81,126 76,122 82.5,122"/>
        <polygon points="108,112 110.5,118 117,118 112,122 114,128 108,124 102,128 104,122 99,118 105.5,118"/>
      </g>
      <rect x="-4" y="70" width="178" height="32" fill="rgba(0,0,0,0)"/>
      <text x="85" y="96" text-anchor="middle" fill="var(--white)" font-family="Montserrat, sans-serif" font-weight="800" font-size="25">APPLY NOW</text>
    </svg>

    <section class="offer">
      <ul class="offer__points">
        <li>- Turn your skills and passion for music into a career -</li>
        <li>- Designed for Musicians, Artists, Producers &amp; Teachers -</li>
      </ul>
      <p class="offer__call">Call 1300 XXX XXX</p>
      <p class="offer__web">www.meridianschoolofmusic.com.au</p>
      <div class="offer__frame"></div>
    </section>
  </main>
</body>
</html>
```